Homeopathic medicinal cream label design

I am looking for a product label design for a medicinal (cannabis) topical cream to be sold to medical marijuana patients. It is a new product that has not yet established a brand identity. It will be sold in 2 and 4 ounce containers so the design needs to work on a small scale. The design may be used for other branding as well.

Target Market(s)

Medical marijuana users in states where it is legal. The product should appeal to both men and women to promote pain relief in muscles and joints. It can also be used as a massage cream for general relaxation.

Industry/Entity Type

Medical

Font styles to use
Sans Serif

Requirements
Must have
• Something that reflects the company name - The Quiet Heron - and the name of the initial product - Meadow Balm Blend.
• In addition to the name of the company and the name of the product, other information to include would be the volume being sold (e.g. 4 oz.), that it is a topical botanical ointment, and its ingredients (coconut oil, beeswax, soy lecithin, and eight all natural botanical oils - cannabis, lavender, eucalyptus, peppermint, rosemary, cinnamon, clove, and lemon). The label should clearly state that the product is for topical use only.
• The information must fit on the space available on the package. The 4 oz. container's lid has approximately 2 1/8" of surface area. The width of the label on the lid should be approximately 1 7/8". On the container's body, the height of the surface area is approximately 1", and the width is approximately 8 1/2 inches. The width of the label should be around 8 inches to allow room for it to be applied to the container. I have posted a photo of the 4 oz. container and the 2 oz. container. I have also posted a photo of the labeling of some of our competitors with similar products.
Nice to have
• We are thinking of having the logo on the lid of the container, and a circle bordering the lid that may have text in it. (See the "Amber Moth" label attached as an exemplar).
• The label on the body of the container (or maybe on the bottom on the container) would list other information about the product, such as its ingredients and our contact information.

```html
<!DOCTYPE html>
<html lang="en">
<head>
<meta charset="utf-8">
<title>The Quiet Heron – Meadow Balm Blend Label</title>
<link href="https://fonts.googleapis.com/css2?family=Open+Sans:wght@400;600;700&family=Chewy&display=swap" rel="stylesheet">
<style>
  :root {
    --paper: #f4f5f1;
    --dot: #e3e6dd;
    --band: #ffffff;
    --leaf-light: #c9e27a;
    --leaf-mid: #8cc63f;
    --leaf-dark: #4f9a3a;
    --heading-bar: #cfe3a3;
    --heading-fade: rgba(207, 227, 163, 0);
    --title-green: #8dc63f;
    --title-stroke: #2f6b1f;
    --text: #3a3a3a;
    --text-soft: #555555;
  }
  * { box-sizing: border-box; margin: 0; padding: 0; }
  html, body { width: 1200px; height: 237px; overflow: hidden; }
  body {
    background: var(--paper);
    font-family: "Open Sans", Arial, sans-serif;
    color: var(--text);
  }
  .label {
    position: relative;
    width: 1200px;
    height: 237px;
    overflow: hidden;
    background-color: var(--paper);
    background-image: radial-gradient(var(--dot) 1.2px, transparent 1.4px);
    background-size: 9px 9px;
  }
  .foliage {
    position: absolute;
    left: 30px;
    width: 1140px;
    border-radius: 40px;
  }
  .foliage--top {
    top: 0;
    height: 80px;
    background: linear-gradient(180deg, rgba(201,226,122,0.25) 0%, var(--leaf-light) 45%, var(--leaf-mid) 100%);
  }
  .foliage--bottom {
    bottom: 0;
    height: 80px;
    background: linear-gradient(0deg, rgba(201,226,122,0.25) 0%, var(--leaf-light) 45%, var(--leaf-mid) 100%);
  }
  .info-band {
    position: absolute;
    left: 71px;
    top: 57px;
    width: 1058px;
    height: 123px;
    background: var(--band);
    box-shadow: 0 0 6px rgba(0,0,0,0.08);
  }
  .section-heading {
    position: absolute;
    font-size: 14px;
    font-weight: 600;
    color: #333;
    padding: 2px 0 2px 8px;
    background: linear-gradient(90deg, var(--heading-bar) 0%, var(--heading-bar) 60%, var(--heading-fade) 100%);
  }
  .ingredients-heading { left: 32px; top: 30px; width: 230px; }
  .ingredients {
    position: absolute;
    left: 40px;
    top: 56px;
    width: 270px;
    font-size: 10px;
    line-height: 13px;
    color: var(--text);
  }
  .ingredients strong { font-weight: 700; }
  .brand {
    position: absolute;
    left: 400px;
    top: 22px;
    width: 150px;
    text-align: center;
  }
  .brand-mark {
    display: block;
    margin: 0 auto 8px;
    width: 44px;
    height: 44px;
    border-radius: 50%;
    background: var(--leaf-mid);
  }
  .brand-name {
    font-size: 17px;
    font-weight: 600;
    color: var(--text-soft);
  }
  .product {
    position: absolute;
    left: 556px;
    top: 22px;
    width: 150px;
    text-align: center;
  }
  .product-name {
    font-family: "Chewy", "Open Sans", sans-serif;
    font-size: 25px;
    line-height: 24px;
    color: var(--title-green);
    -webkit-text-stroke: 1px var(--title-stroke);
    letter-spacing: 0.5px;
    text-transform: uppercase;
  }
  .product-volume {
    text-align: right;
    font-size: 10px;
    font-weight: 700;
    color: #222;
    margin-top: 2px;
  }
  .contact-heading { left: 783px; top: 14px; width: 220px; }
  .contact {
    position: absolute;
    left: 783px;
    top: 44px;
    font-size: 12px;
    line-height: 17px;
    color: var(--text-soft);
    font-style: normal;
  }
</style>
</head>
<body>
  <div class="label">
    <div class="foliage foliage--top" role="img" aria-label="Illustrated green leaves framing the top of the label"></div>
    <div class="foliage foliage--bottom" role="img" aria-label="Illustrated green leaves framing the bottom of the label"></div>

    <section class="info-band">
      <h2 class="section-heading ingredients-heading">Topical Botanical Ointment</h2>
      <p class="ingredients"><strong>Ingredients :</strong> coconut oil, beeswax, soy lecithin, and eight all natural botanical oils - cannabis, lavender, eucalyptus, peppermint, rosemary, cinnamon, clove, and lemon</p>

      <div class="brand">
        <span class="brand-mark" aria-hidden="true"></span>
        <p class="brand-name">The Quiet Heron</p>
      </div>

      <div class="product">
        <h1 class="product-name">Meadow Balm<br>Blend</h1>
        <p class="product-volume">4oz.</p>
      </div>

      <h2 class="section-heading contact-heading">Contact Information</h2>
      <address class="contact">
        Dana &amp; Rowan Ellery, 5820 Saltmarsh Lane<br>
        Cedar Key, FL 32625<br>
        Phone: 1-800-555-01982<br>
        Web: www.quietheronbalm.com
      </address>
    </section>
  </div>
</body>
</html>
```